Business Card Design for Consulting Company

I require a Business Card design for my Consulting company. <br/><br/>My company name is: Marek Olvani Consulting Inc.<br/>My website is: www.marekolvaniconsulting.example<br/><br/>My company focuses on management and software development for the Tallobrix CRM platform (www.tallobrix.example)<br/><br/>I have a logo already designed...see attached.
Updates

Also Include my Name and Title: Marek T.L. Olvani President

Target Market(s)

Tallobrix Customers

Contact Information for Business Card

Only include my LOGO (provided)
My Name: Marek TL Olvani
My Title: President
My Company Name: Marek Olvani Consulting Inc.
My Website: www.marekolvaniconsulting.example
My Email: marek.olvani.consulting@mailbox.example

NO PHONE NUMBER
NO ADDRESS

Font styles to use
Serif
Sans Serif
Other font styles liked:
• see my website: www.marekolvaniconsulting.example

Colors

Designer to choose colors to be used in the design.

Requirements
Must have
• Must include my Orange
• Include my name (Marek T.L. Olvani), title (President) company name, website and email
• It should also have a tag line like: Tallobrix Consulting
• I'm flexible with the tag line
Should not have
• Don't include my phone number or address

```html
<!DOCTYPE html>
<html lang="en">
<head>
<meta charset="utf-8">
<title>Marek Olvani Consulting Inc. – Business Card</title>
<link rel="stylesheet" href="https://fonts.googleapis.com/css2?family=Arimo:ital,wght@0,400;0,700;1,400&display=swap">
<style>
  :root {
    --brand-orange: #f38220;
    --card-white: #ffffff;
    --text-grey: #6b6b6b;
    --stage: #4a4a4a;
  }
  * { box-sizing: border-box; margin: 0; padding: 0; }
  html, body {
    width: 1200px;
    height: 1200px;
    overflow: hidden;
    background: var(--stage);
    font-family: "Arimo", Arial, sans-serif;
  }
  .stage {
    position: relative;
    width: 1200px;
    height: 1200px;
  }
  .card {
    position: absolute;
    left: 230px;
    width: 740px;
    height: 420px;
    border-radius: 26px;
    overflow: hidden;
    box-shadow: 0 10px 28px rgba(0,0,0,0.35);
  }
  /* Back side */
  .card--back {
    top: 130px;
    background: var(--brand-orange);
    display: flex;
    align-items: center;
    justify-content: center;
  }
  .brand-mark {
    display: flex;
    align-items: center;
    gap: 18px;
    font-weight: 700;
    letter-spacing: 0.5px;
  }
  .brand-mark__square {
    width: 34px;
    height: 34px;
    background: currentColor;
  }
  .card--back .brand-mark {
    color: var(--card-white);
    font-size: 54px;
  }
  /* Front side */
  .card--front {
    top: 640px;
    background: var(--card-white);
  }
  .card--front .brand-mark {
    position: absolute;
    left: 40px;
    top: 118px;
    color: var(--brand-orange);
    font-size: 30px;
    gap: 12px;
  }
  .card--front .brand-mark__square {
    width: 22px;
    height: 22px;
  }
  .contact {
    position: absolute;
    left: 318px;
    top: 92px;
    width: 400px;
  }
  .contact__name {
    color: var(--brand-orange);
    font-weight: 700;
    font-size: 30px;
    line-height: 1.05;
  }
  .contact__title {
    color: var(--text-grey);
    font-size: 21px;
    margin-bottom: 26px;
  }
  .contact__company {
    color: var(--brand-orange);
    font-weight: 700;
    font-size: 21px;
    margin-bottom: 8px;
  }
  .contact__line {
    display: flex;
    align-items: center;
    gap: 8px;
    color: var(--text-grey);
    font-size: 16.5px;
    line-height: 1.5;
    white-space: nowrap;
  }
  .contact__icon {
    width: 16px;
    height: 16px;
    flex: none;
  }
  .tagline-band {
    position: absolute;
    left: 0;
    bottom: 0;
    width: 100%;
    height: 62px;
    background: var(--brand-orange);
    color: var(--card-white);
    font-size: 22px;
    display: flex;
    align-items: center;
    padding-left: 190px;
  }
</style>
</head>
<body>
<main class="stage">
  <section class="card card--back" aria-label="Card back">
    <div class="brand-mark">
      <span class="brand-mark__square"></span>
      <span>Marek Olvani</span>
    </div>
  </section>

  <section class="card card--front" aria-label="Card front">
    <div class="brand-mark">
      <span class="brand-mark__square"></span>
      <span>Marek Olvani</span>
    </div>

    <div class="contact">
      <p class="contact__name">Marek TL Olvani</p>
      <p class="contact__title">President</p>
      <p class="contact__company">Marek Olvani Consulting Inc.</p>
      <p class="contact__line">
        <svg class="contact__icon" viewBox="0 0 16 16" aria-hidden="true">
          <rect x="1" y="3" width="14" height="10" fill="var(--brand-orange)"/>
          <path d="M1 3 L8 9 L15 3 M1 13 L6 7.5 M15 13 L10 7.5" stroke="#fff" stroke-width="1.3" fill="none"/>
        </svg>
        marek.olvani.consulting@mailbox.example
      </p>
      <p class="contact__line">
        <svg class="contact__icon" viewBox="0 0 16 16" aria-hidden="true">
          <g fill="none" stroke="var(--brand-orange)" stroke-width="1.3">
            <circle cx="8" cy="8" r="6.5"/>
            <ellipse cx="8" cy="8" rx="3" ry="6.5"/>
            <path d="M1.5 8 H14.5 M2.5 4.8 H13.5 M2.5 11.2 H13.5"/>
          </g>
        </svg>
        www.marekolvaniconsulting.example
      </p>
    </div>

    <div class="tagline-band">Tallobrix Consulting</div>
  </section>
</main>
</body>
</html>
```